KLOMB Systems website

We need a website design using much of the information on the KLOMB flyer (attached) we just had a PixelBarn designer create. We'd like a WordPress Site, no need for a shopping cart attached to it. It should have an About us page, Book titles page, a blog page, Membership and Navigators pages contact us and privacy policy and terms of services.

```html
<!DOCTYPE html>
<html lang="en">
<head>
<meta charset="utf-8">
<title>KLOMB Systems</title>
<link href="https://fonts.googleapis.com/css2?family=Open+Sans:wght@400;600;700&display=swap" rel="stylesheet">
<style>
:root{
  --brand:#2e4f86;
  --brand-dark:#203a66;
  --brand-light:#4a74b8;
  --ink:#333;
  --muted:#555;
  --white:#fff;
  --grey-band:#efefef;
  --footer:#2b2b2b;
}
*{margin:0;padding:0;box-sizing:border-box}
html,body{width:1200px;height:3077px;overflow:hidden}
body{font-family:"Open Sans",Arial,sans-serif;color:var(--ink);background:var(--white);position:relative}
.abs{position:absolute}

/* header */
.site-header{position:absolute;left:0;top:0;width:1200px;height:123px;background:var(--white)}
.brand-name{position:absolute;left:133px;top:44px;font-size:42px;font-weight:700;color:var(--brand);letter-spacing:1px}
.phone{position:absolute;right:133px;top:30px;font-size:22px;font-weight:600;color:var(--brand);display:flex;align-items:center;gap:8px}
.main-nav{position:absolute;right:133px;top:84px;display:flex;gap:40px;font-size:16px;color:#444;white-space:nowrap}
.main-nav .current{color:var(--brand)}

/* hero */
.hero{position:absolute;left:0;top:123px;width:1200px;height:492px;background:linear-gradient(120deg,#4f7fc4 0%,#2f5a9c 45%,#1b3565 100%)}
.hero-title{position:absolute;left:0;width:1200px;top:190px;text-align:center;color:var(--white);font-size:48px;font-weight:700;line-height:58px}
.hero-arrow{position:absolute;top:230px;width:28px;height:28px;background:#111;display:flex;align-items:center;justify-content:center}

/* benefits */
.section-title{position:absolute;left:0;width:1200px;text-align:center;color:var(--brand);font-weight:700}
.benefits-title{top:688px;font-size:40px;line-height:50px}
.benefit-card{position:absolute;top:804px;width:294px;height:388px;background:var(--brand)}
.benefit-card .card-head{height:205px;position:relative;border-bottom:1px solid rgba(255,255,255,.4)}
.benefit-card .icon{position:absolute;left:14px;top:18px}
.benefit-card .kicker{position:absolute;left:15px;top:118px;color:var(--white);font-size:17px;font-weight:700}
.benefit-card .name{position:absolute;left:15px;top:136px;color:var(--white);font-size:40px;font-weight:600;white-space:nowrap}
.benefit-card ul{list-style:none;padding:18px 18px 0 16px}
.benefit-card li{color:var(--white);font-size:11.5px;line-height:17px;margin-bottom:14px;padding-left:18px;position:relative}
.benefit-card li::before{content:"›";position:absolute;left:0;top:-3px;font-size:18px;font-weight:700}

/* growth band */
.growth{position:absolute;left:0;top:1272px;width:1200px;height:806px;background:linear-gradient(135deg,#3b5f97 0%,#28487d 50%,#1f3a68 100%)}
.growth-title{position:absolute;left:0;width:1200px;top:93px;text-align:center;color:var(--white);font-size:40px;font-weight:700;line-height:48px}
.pyramid-sub{position:absolute;left:499px;width:200px;top:1640px;text-align:center;font-size:14px;line-height:21px;color:#555}
.pyramid-list{position:absolute;left:440px;width:320px;top:1704px;text-align:center}
.pyramid-line{font-size:28px;font-weight:600;color:var(--brand);height:57px;line-height:57px;border-bottom:1px solid #ccc;width:290px;margin:0 auto;white-space:nowrap}
.pyramid-line:last-child{border-bottom:none}
.badge{position:absolute;width:82px;height:82px;border-radius:50%;background:#2d2d2d;border:5px solid var(--white);display:flex;align-items:center;justify-content:center}

/* blog */
.blog-title{top:2146px;font-size:40px}
.post{position:absolute;top:2221px;width:300px}
.post .thumb{width:300px;height:173px}
.post h3{font-size:15px;font-weight:400;color:var(--brand);margin-top:14px;white-space:nowrap}
.post .meta{font-size:13px;color:#333;margin-top:10px;display:flex;gap:22px}
.post p{font-size:11px;line-height:16px;color:var(--muted);margin-top:8px}
.post .more{display:inline-block;margin-top:14px;font-size:12px;color:#222;text-decoration:underline}
.blog-arrow{position:absolute;top:2300px;width:20px;height:32px}

/* membership */
.membership{position:absolute;left:0;top:2656px;width:1200px;height:308px;background:var(--grey-band)}
.membership h2{position:absolute;left:0;width:1200px;top:68px;text-align:center;color:var(--brand);font-size:40px;font-weight:700}
.membership p{position:absolute;left:150px;width:900px;top:122px;text-align:center;font-size:16.5px;line-height:24px;color:#333}
.register-btn{position:absolute;left:525px;top:181px;width:148px;height:45px;background:var(--brand);color:var(--white);font-size:15px;font-weight:600;display:flex;align-items:center;justify-content:center}

/* footer */
.site-footer{position:absolute;left:0;top:2964px;width:1200px;height:113px;background:var(--footer);color:#bbb}
.footer-nav{position:absolute;left:133px;top:29px;font-size:11px;display:flex;gap:10px}
.footer-nav span.sep{color:#888}
.copyright{position:absolute;left:133px;top:62px;font-size:11px}
.social{position:absolute;top:42px;width:16px;height:16px;border-radius:50%;background:#bbb}
</style>
</head>
<body>

<header class="site-header">
  <div class="brand-name">KLOMB</div>
  <div class="phone">
    <svg width="18" height="18" viewBox="0 0 24 24"><path fill="#2e4f86" d="M6.6 10.8a15 15 0 0 0 6.6 6.6l2.2-2.2c.3-.3.7-.4 1-.2 1.1.4 2.3.6 3.6.6.6 0 1 .4 1 1V20c0 .6-.4 1-1 1A17 17 0 0 1 3 4c0-.6.4-1 1-1h3.5c.6 0 1 .4 1 1 0 1.3.2 2.5.6 3.6.1.3 0 .7-.2 1z"/></svg>
    800-555-0142
  </div>
  <nav class="main-nav">
    <span class="current">Home</span><span>About us</span><span>Book Titles</span><span>Blog</span><span>Membership</span><span>Contact us</span>
  </nav>
</header>

<section class="hero" role="img" aria-label="Blue-tinted photo of a desk with laptop, charts and a hand holding a pen">
  <h1 class="hero-title">ACCELERATE YOUR<br>BUSINESS WITH KLOMB™!</h1>
  <div class="hero-arrow" style="left:0"><svg width="14" height="14" viewBox="0 0 14 14"><path d="M12 7H3M6 3L2 7l4 4" stroke="#fff" stroke-width="2" fill="none"/></svg></div>
  <div class="hero-arrow" style="right:0"><svg width="14" height="14" viewBox="0 0 14 14"><path d="M2 7h9M8 3l4 4-4 4" stroke="#fff" stroke-width="2" fill="none"/></svg></div>
</section>

<h2 class="section-title benefits-title">BECOME A KLOMB™ MEMBER TODAY<br>AND YOU WILL RECEIVE...</h2>

<article class="benefit-card" style="left:133px">
  <div class="card-head">
    <svg class="icon" width="82" height="82" viewBox="0 0 82 82" fill="none" stroke="#fff" stroke-width="2"><rect x="30" y="6" width="34" height="24"/><path d="M38 18l5 5 10-10"/><circle cx="18" cy="22" r="6"/><path d="M10 50V34h16l10-6M18 34v40"/><circle cx="38" cy="58" r="4"/><circle cx="52" cy="58" r="4"/><circle cx="66" cy="58" r="4"/><rect x="33" y="64" width="10" height="10"/><rect x="47" y="64" width="10" height="10"/><rect x="61" y="64" width="10" height="10"/></svg>
    <div class="kicker">KLOMB™</div>
    <div class="name">Coaching</div>
  </div>
  <ul>
    <li>Coaching for you and your leadership team</li>
    <li>Launch pad, monthly and quarterly touchpoints, annual planning</li>
    <li>Continuous learning model</li>
    <li>All KLOMB coaches are successful million-dollar entrepreneurs (our Navigators)</li>
  </ul>
</article>

<article class="benefit-card" style="left:453px">
  <div class="card-head">
    <svg class="icon" width="82" height="82" viewBox="0 0 82 82" fill="none" stroke="#fff" stroke-width="2"><rect x="28" y="6" width="26" height="20" rx="2"/><path d="M34 13h14M34 19h14M41 26v12M16 38h50M16 38v10M41 38v10M66 38v10"/><rect x="6" y="48" width="20" height="22"/><rect x="31" y="48" width="20" height="22"/><rect x="56" y="48" width="20" height="22"/><path d="M10 55h12M10 62h12M35 55h12M35 62h12M60 55h12M60 62h12"/></svg>
    <div class="kicker">KLOMB™</div>
    <div class="name">Structure</div>
  </div>
  <ul>
    <li>Structured program that ensures focus, productivity and accountability</li>
    <li>Robust collection of simple, streamlined tools and processes</li>
    <li>KLOMB Strategy Stack – for clarity and alignment</li>
  </ul>
</article>

<article class="benefit-card" style="left:773px">
  <div class="card-head">
    <svg class="icon" width="82" height="82" viewBox="0 0 82 82" fill="none" stroke="#fff" stroke-width="2"><circle cx="28" cy="28" r="12"/><circle cx="28" cy="28" r="5"/><path d="M28 8v6M28 42v6M8 28h6M42 28h6M14 14l4 4M38 38l4 4M14 42l4-4M38 18l4-4"/><circle cx="56" cy="56" r="10"/><circle cx="56" cy="56" r="4"/><path d="M56 40v5M56 67v5M40 56h5M67 56h5M45 45l3 3M64 64l3 3M45 67l3-3M64 48l3-3"/></svg>
    <div class="kicker">KLOMB™</div>
    <div class="name">Resources</div>
  </div>
  <ul>
    <li>Pre-packaged business processes</li>
    <li>Simplified business templates and forms</li>
    <li>Online, self-paced learning library</li>
    <li>Technology platform for tracking and accountability</li>
  </ul>
</article>

<section class="growth" role="img" aria-label="Blue-tinted photo of people reviewing charts and a laptop on a desk">
  <h2 class="growth-title">HOW KLOMB™ ACCELERATES YOUR BUSINESS<br>GROWTH!</h2>
</section>

<svg class="abs" style="left:0;top:0" width="1200" height="2078" viewBox="0 0 1200 2078">
  <polygon points="599,1560 362,1935 836,1935" fill="#fff" stroke="#fff" stroke-width="70" stroke-linejoin="round"/>
</svg>

<div class="badge" style="left:558px;top:1487px">
  <svg width="40" height="40" viewBox="0 0 82 82" fill="none" stroke="#fff" stroke-width="4"><rect x="30" y="6" width="34" height="24"/><circle cx="18" cy="22" r="6"/><path d="M18 34v40M10 34h16"/><rect x="33" y="60" width="10" height="12"/><rect x="47" y="60" width="10" height="12"/><rect x="61" y="60" width="10" height="12"/></svg>
</div>
<div class="badge" style="left:287px;top:1893px">
  <svg width="40" height="40" viewBox="0 0 82 82" fill="none" stroke="#fff" stroke-width="4"><rect x="28" y="6" width="26" height="20"/><path d="M41 26v12M16 38h50M16 38v10M41 38v10M66 38v10"/><rect x="6" y="48" width="20" height="22"/><rect x="31" y="48" width="20" height="22"/><rect x="56" y="48" width="20" height="22"/></svg>
</div>
<div class="badge" style="left:831px;top:1893px">
  <svg width="40" height="40" viewBox="0 0 82 82" fill="none" stroke="#fff" stroke-width="4"><circle cx="28" cy="28" r="12"/><path d="M28 8v6M28 42v6M8 28h6M42 28h6"/><circle cx="56" cy="56" r="10"/><path d="M56 40v5M56 67v5M40 56h5M67 56h5"/></svg>
</div>

<p class="pyramid-sub">A Simple, Comprehensive Coaching System for Small Businesses</p>
<div class="pyramid-list">
  <div class="pyramid-line">THE RIGHT COACH</div>
  <div class="pyramid-line">THE RIGHT SYSTEM</div>
  <div class="pyramid-line">THE RIGHT TOOLS</div>
  <div class="pyramid-line">THE RIGHT PRICE</div>
</div>

<h2 class="section-title blog-title">BLOG</h2>
<svg class="blog-arrow" style="left:54px" viewBox="0 0 20 32"><path d="M16 4L4 16l12 12" stroke="#666" stroke-width="2.5" fill="none"/></svg>
<svg class="blog-arrow" style="left:1126px" viewBox="0 0 20 32"><path d="M4 4l12 12L4 28" stroke="#666" stroke-width="2.5" fill="none"/></svg>

<article class="post" style="left:133px">
  <div class="thumb" role="img" aria-label="Photo of a businessman working on a laptop in an office" style="background:linear-gradient(135deg,#cfd3d6,#6f7780 60%,#3a3f45)"></div>
  <h3>Curabitur venenatis lacinia ornare</h3>
  <div class="meta"><span>▦ 3 Oct, 2018</span><span>● Admin</span></div>
  <p>Maecenas vel tortor accumsan quam varius imperdiet vel eget elit. Aenean facilisis tincidunt lectus, id dictum nisi luctus eget. Vivamus efficitur ex condimentum, malesuada eros eget.</p>
  <span class="more">READ MORE</span>
</article>
<article class="post" style="left:451px">
  <div class="thumb" role="img" aria-label="Photo of hands using a tablet showing charts" style="background:linear-gradient(135deg,#3a3a3a,#7a7268 50%,#d8c7b0)"></div>
  <h3>Quisque aliquet ex nec est vestibulum</h3>
  <div class="meta"><span>▦ 3 Oct, 2018</span><span>● Admin</span></div>
  <p>Etiam mattis augue vehicula odio posuere, sit amet tempus lectus luctus. Nulla facilisi. Etiam vel massa elementum, bibendum tellus venenatis, feugiat massa. Curabitur venenatis lacinia ornare.</p>
  <span class="more">READ MORE</span>
</article>
<article class="post" style="left:767px">
  <div class="thumb" role="img" aria-label="Overhead photo of a team meeting around a wooden table" style="background:linear-gradient(135deg,#6b4a33,#9a7656 50%,#4a3424)"></div>
  <h3>Pellentesque convallis molestie enim</h3>
  <div class="meta"><span>▦ 3 Oct, 2018</span><span>● Admin</span></div>
  <p>Aliquam erat volutpat. Quisque aliquet ex nec est vestibulum pulvinar. Pellentesque convallis molestie enim sit amet efficitur. Etiam id imperdiet lectus. Vivamus lacus justo, ultrices nec erat in, euismod iaculis.</p>
  <span class="more">READ MORE</span>
</article>

<section class="membership">
  <h2>MEMBERSHIP</h2>
  <p>Maecenas vel tortor accumsan quam varius imperdiet vel eget elit. Aenean facilisis tincidunt lectus, id dictum nisi luctus eget. Vivamus efficitur ex condimentum, malesuada eros eget, feugiat nibh.</p>
  <div class="register-btn">REGISTER NOW</div>
</section>

<footer class="site-footer">
  <nav class="footer-nav">
    <span>Home</span><span class="sep">|</span><span>About us</span><span class="sep">|</span><span>Book Titles</span><span class="sep">|</span><span>Blog</span><span class="sep">|</span><span>Membership</span><span class="sep">|</span><span>Contact us</span><span class="sep">|</span><span>Privacy Policy</span><span class="sep">|</span><span>Terms of Service</span>
  </nav>
  <div class="copyright">Copyright © 2018 KLOMB Systems. All rights reserved.</div>
  <div class="social" style="left:1006px"></div>
  <div class="social" style="left:1048px"></div>
</footer>

</body>
</html>
```